District Manager Business Card

Hello, I own 3 automotive repair shops that are all 3 different names. I need a card that has all 3 locations and logos on it. Just a simple, modern, clean design. I selected double sided, but If a single side is more ideal, thats ok too. I am open to explore both options. I attached the 3 logos in a few different formats.

Industry/Entity Type

Auto Repair

Contact Information for Business Card

Requirements
Must have
• Location information:
Q&L Automotive
482 Birchfield Ave.
Crossville TN 38555

MOTO MEND
257 Pine Hollow Turnpike
Oak Ridge TN 37830

Brantmoor Tire & Auto
614 North Aspen Ave.
Cookeville TN 38501

District Manager - Dale Hobart - Dale@qandlauto-example.com - Cell: 931-555-0196
Nice to have
• This can be a single or a double sided card. Just want a clean card that shows all 3 locations.

```html
<!DOCTYPE html>
<html lang="en">
<head>
<meta charset="utf-8">
<title>Dale Hobart – District Manager Card</title>
<link rel="stylesheet" href="https://fonts.googleapis.com/css2?family=Montserrat:wght@400;500;700;800&display=swap">
<style>
  :root {
    --backdrop: #e9e6e1;
    --yellow: #ece91f;
    --red: #e5131b;
    --black: #262628;
    --white: #ffffff;
    --navy: #2b2e8f;
    --ink: #4a4a4a;
  }
  * { box-sizing: border-box; margin: 0; padding: 0; }
  html, body {
    width: 1200px; height: 1023px; overflow: hidden;
    background: var(--backdrop);
    font-family: "Montserrat", Arial, sans-serif;
  }
  .card {
    position: absolute; left: 75px; top: 211px;
    width: 1050px; height: 600px;
    border-radius: 22px; overflow: hidden;
    box-shadow: 0 18px 40px rgba(0,0,0,.25);
    background: var(--white);
  }
  .card-shapes { position: absolute; inset: 0; }
  .location { position: absolute; top: 70px; width: 300px; }
  .location-name { font-weight: 800; font-size: 26px; letter-spacing: .5px; line-height: 1.1; }
  .location-address { margin-top: 16px; font-size: 20px; line-height: 1.3; }
  .location--ql { left: 40px; color: var(--navy); }
  .location--ql .location-address { color: var(--ink); }
  .location--moto { left: 395px; color: var(--white); }
  .location--brant { left: 735px; color: var(--white); }
  .manager { position: absolute; left: 390px; top: 315px; }
  .manager-name { color: var(--red); font-weight: 800; font-size: 40px; letter-spacing: .5px; }
  .manager-title { color: var(--navy); font-weight: 500; font-size: 26px; margin-top: 4px; }
  .contacts {
    position: absolute; left: 160px; top: 478px;
    display: flex; gap: 70px; align-items: center;
    color: var(--white); font-size: 26px; font-weight: 500;
  }
  .contact { display: flex; align-items: center; gap: 14px; }
  .contact-icon { width: 32px; height: 32px; }
</style>
</head>
<body>
<div class="card">
  <svg class="card-shapes" viewBox="0 0 1050 600" width="1050" height="600" aria-hidden="true">
    <rect x="0" y="0" width="1050" height="600" fill="var(--white)"/>
    <polygon points="0,0 370,0 340,280 0,280" fill="var(--yellow)"/>
    <polygon points="370,0 720,0 690,280 340,280" fill="var(--red)"/>
    <polygon points="720,0 1050,0 1050,280 690,280" fill="var(--black)"/>
    <polygon points="0,448 1050,448 1050,454 0,454" fill="var(--yellow)"/>
    <rect x="0" y="454" width="1050" height="100" fill="var(--red)"/>
    <rect x="0" y="554" width="1050" height="46" fill="var(--navy)"/>
  </svg>

  <div class="location location--ql">
    <div class="location-name">Q&amp;L AUTOMOTIVE</div>
    <div class="location-address">482 Birchfield Ave.<br>Crossville TN 38555</div>
  </div>
  <div class="location location--moto">
    <div class="location-name">MOTO MEND</div>
    <div class="location-address">257 Pine Hollow Turnpike<br>Oak Ridge TN 37830</div>
  </div>
  <div class="location location--brant">
    <div class="location-name">BRANTMOOR TIRE &amp; AUTO</div>
    <div class="location-address">614 North Aspen Ave.<br>Cookeville TN 38501</div>
  </div>

  <div class="manager">
    <div class="manager-name">DALE HOBART</div>
    <div class="manager-title">District Manager</div>
  </div>

  <div class="contacts">
    <div class="contact">
      <svg class="contact-icon" viewBox="0 0 32 32" aria-hidden="true">
        <circle cx="16" cy="16" r="16" fill="var(--navy)"/>
        <path d="M11 9l3 0 1.5 4-2 1.5a9 9 0 0 0 4 4l1.5-2 4 1.5 0 3a2 2 0 0 1-2 2A14 14 0 0 1 9 11a2 2 0 0 1 2-2z" fill="var(--white)"/>
      </svg>
      <span>931-555-0196</span>
    </div>
    <div class="contact">
      <svg class="contact-icon" viewBox="0 0 32 32" aria-hidden="true">
        <circle cx="16" cy="16" r="16" fill="var(--navy)"/>
        <rect x="8" y="10" width="16" height="12" rx="1.5" fill="none" stroke="var(--white)" stroke-width="2"/>
        <path d="M8.5 11l7.5 6 7.5-6" fill="none" stroke="var(--white)" stroke-width="2"/>
      </svg>
      <span>Dale@qandlauto-example.com</span>
    </div>
  </div>
</div>
</body>
</html>
```